New web design for software product company

Our company, Tracvenna, does big data analytics for system monitoring and root cause analysis. We help large enterprise IT organisations improve service levels and increase efficiency through searching, analysing and visualising log data.

We need a new design for www.tracvenna-example.com.

The primary goal of the site is to drive visitors to download our product.

We are launching a new 2.0 version of our product in mid-July. In addition to updating our web design, we will need to replace all of the current product images on the current site. We have attached several sample images of the new product to help you with your design.

We would like to reuse the existing textual content, videos and logo on the current site.

Industry/Entity Type

It Company

Requirements
Must have
• We would like flat design, and we would like the new site to be responsive and SEO-friendly.

We need to have our customer logos on the front page.

We would expect to receive handcrafted and maintainable css and html files as well as any new images created by the designer. The maintainability of these files is essential.
Nice to have
• We prefer a bootstrap-based design.
Should not have
• Our target audience is a technical end user who works in a large enterprise IT organisation, typically in a support or operational role, e.g. applications, operations or infrastructure support.

```html
<!DOCTYPE html>
<html lang="en">
<head>
<meta charset="utf-8">
<title>Tracvenna – Real-time log analytics</title>
<link href="https://fonts.googleapis.com/css2?family=Roboto:ital,wght@0,300;0,400;0,500;0,700;1,400;1,700&display=swap" rel="stylesheet">
<style>
:root{
  --blue:#2f5fd6;
  --blue-link:#3a63c9;
  --header-dark:#2a2a2a;
  --text:#444;
  --border:#d4d4d4;
  --band:#eeeeef;
  --footer:#353535;
  --footer-text:#cfcfcf;
}
*{box-sizing:border-box;margin:0;padding:0}
html,body{width:850px;height:1200px;overflow:hidden}
body{font-family:"Roboto",Arial,sans-serif;color:var(--text);background:#fff;position:relative}
a{color:inherit;text-decoration:none}

.site-header{position:absolute;top:0;left:0;width:850px;height:77px;background:linear-gradient(#3d3d3d,var(--header-dark))}
.brand{position:absolute;left:92px;top:24px;display:flex;align-items:center;gap:10px;color:#fff;font-weight:700;font-size:26px;letter-spacing:1px}
.brand-mark{width:22px;height:22px;border-radius:50%;background:var(--blue)}
.main-nav{position:absolute;right:92px;top:31px;font-size:11px;color:#eee;display:flex;gap:8px}
.main-nav span.sep{color:#bbb}

.hero{position:absolute;top:77px;left:0;width:850px;height:303px;background:linear-gradient(#fafafa,#e7e7e7);border-bottom:2px solid #d6d6d6}
.hero-device{position:absolute;left:102px;top:57px;width:388px;height:246px;border-radius:10px 10px 0 0;background:linear-gradient(135deg,#c9d2e6,#e8ecf2 50%,#a9c8a6);border:6px solid #2c2c2c;border-bottom:none}
.hero-copy{position:absolute;left:513px;top:52px;width:250px}
.hero-title{font-size:22px;font-weight:700;font-style:italic;color:var(--blue);line-height:27px}
.hero-title .lead-a{font-weight:400;font-style:normal;color:#333;font-size:18px}
.hero-sub{font-size:17px;font-weight:300;color:#333;margin-top:1px}
.hero-tagline{font-size:16px;font-weight:300;color:var(--blue);line-height:21px;margin-top:17px}
.btn-dark{display:inline-block;margin-top:28px;margin-left:2px;background:#333;color:#fff;font-size:11.5px;font-weight:500;padding:7px 14px;border-radius:3px}
.hero-dots{position:absolute;left:699px;top:277px;display:flex;gap:4px}
.hero-dots i{width:11px;height:11px;border-radius:50%;background:#777}
.hero-dots i:first-child{background:#333}

.download-bar{position:absolute;left:92px;top:397px;width:666px;height:69px;border:1px solid var(--border);border-radius:3px;background:#f6f6f6}
.download-bar p{position:absolute;left:15px;top:25px;font-size:14px;font-weight:300;color:#333}
.btn-primary{position:absolute;left:518px;top:18px;width:133px;height:30px;background:var(--blue);color:#fff;font-size:11px;font-weight:700;text-align:center;line-height:30px;border-radius:3px;letter-spacing:.4px}

.about{position:absolute;left:125px;top:480px;width:600px;text-align:center}
.about h2{font-size:18px;font-weight:400;color:var(--blue)}
.about p{font-size:10.3px;line-height:16.5px;margin-top:5px;color:#444}

.podcast-band{position:absolute;top:570px;left:0;width:850px;height:236px;background:var(--band)}
.section-title{position:absolute;left:93px;top:18px;font-size:16.5px;font-weight:400;color:var(--blue)}
.carousel-arrows{position:absolute;left:726px;top:20px;display:flex;gap:6px}
.video-card{position:absolute;left:92px;top:48px;width:326px;height:171px;border:1px solid var(--border);background:#fbfbf8}
.video-still{position:absolute;left:0;top:0;width:190px;height:169px;background:linear-gradient(90deg,#d9c6b4,#efe6dc)}
.video-meta{position:absolute;left:201px;top:64px}
.video-meta h3{font-size:12.5px;font-weight:500;color:#333}
.video-meta em{display:block;font-size:9px;color:var(--blue);line-height:12px;margin-top:3px}
.play{display:flex;align-items:center;gap:8px;margin-top:10px;font-size:9px;color:#444}
.play-icon{width:29px;height:29px;border-radius:50%;background:#333;display:flex;align-items:center;justify-content:center}
.testimonial{position:absolute;left:442px;top:97px;width:312px}
.testimonial blockquote{font-size:9.4px;font-style:italic;line-height:16.5px;color:#555}
.testimonial cite{display:block;font-style:normal;font-size:8.5px;color:var(--blue-link);margin-top:6px}
.read-more{font-size:9.5px;color:#333}
.testimonial .read-more{display:block;margin-top:37px}

.news-panel{position:absolute;top:821px;width:326px;height:158px;border:1px solid var(--border);border-radius:3px;background:linear-gradient(#f4f4f4,#fff 40%)}
.news-panel.left{left:92px}
.news-panel.right{left:432px}
.news-panel h3{position:absolute;left:12px;top:10px;font-size:13px;font-weight:400;color:#222}
.news-list{position:absolute;left:12px;top:33px;list-style:none}
.news-list li{margin-bottom:7px}
.news-list b{display:table;font-size:10.5px;font-weight:500;color:var(--blue);border-bottom:1px solid var(--blue);line-height:12px}
.news-list p{font-size:8.6px;color:#333;line-height:11px}
.news-list p .src{color:var(--blue-link)}
.news-panel .read-more{position:absolute;left:13px;top:131px}

.clients{position:absolute;top:993px;left:0;width:850px;height:80px;background:#f1f1f1}
.clients ul{list-style:none;position:absolute;left:92px;top:0;width:666px;height:80px;display:flex;justify-content:space-between;align-items:center}
.clients li{font-size:20px;font-weight:700;color:#333}

.site-footer{position:absolute;top:1073px;left:0;width:850px;height:127px;background:var(--footer);color:var(--footer-text)}
.footer-col{position:absolute;top:22px}
.footer-col h4{font-size:11px;font-weight:500;color:#fff;margin-bottom:7px}
.footer-col li{list-style:none;font-size:8.5px;line-height:19px}
.footer-col.connect li{padding-left:18px}
.copyright{position:absolute;left:635px;top:88px;font-size:8.3px;line-height:16px}
</style>
</head>
<body>

<header class="site-header">
  <a class="brand" href="#"><span class="brand-mark"></span>TRACVENNA</a>
  <nav class="main-nav">
    <a href="#">About Us</a><span class="sep">|</span>
    <a href="#">Products</a><span class="sep">|</span>
    <a href="#">Apps</a><span class="sep">|</span>
    <a href="#">Pricing</a><span class="sep">|</span>
    <a href="#">Try</a><span class="sep">|</span>
    <a href="#">Buy</a><span class="sep">|</span>
    <a href="#">Support</a><span class="sep">|</span>
    <a href="#">Contact</a>
  </nav>
</header>

<section class="hero">
  <div class="hero-device" role="img" aria-label="Laptop showing the Tracvenna monitoring dashboard with host, VM, CPU and memory charts"></div>
  <div class="hero-copy">
    <h1 class="hero-title"><span class="lead-a">A</span> “SINGLE PANE OF GLASS”</h1>
    <p class="hero-sub">for DevOps and Monitoring..</p>
    <p class="hero-tagline">Real-Time visibility across<br>Your Entire Technology Stack</p>
    <a class="btn-dark" href="#">Learn More</a>
  </div>
  <div class="hero-dots"><i></i><i></i><i></i><i></i></div>
</section>

<div class="download-bar">
  <p>Big data analytics for real-time system monitoring and root cause analysis</p>
  <a class="btn-primary" href="#">FREE DOWNLOAD »</a>
</div>

<section class="about">
  <h2>About Tracvenna</h2>
  <p>Tracvenna, does big data analytics for system monitoring and root cause analysis. We help large enterprise<br>IT organisations improve service levels and increase efficiency through searching, analysing and visualising<br>log data.</p>
</section>

<section class="podcast-band">
  <h2 class="section-title">Video Poscasts</h2>
  <div class="carousel-arrows">
    <svg width="12" height="16" viewBox="0 0 12 16"><path d="M9 2 3 8l6 6" fill="none" stroke="#444" stroke-width="2"/></svg>
    <svg width="12" height="16" viewBox="0 0 12 16"><path d="M3 2l6 6-6 6" fill="none" stroke="#444" stroke-width="2"/></svg>
  </div>
  <div class="video-card">
    <div class="video-still" role="img" aria-label="Video still of a customer speaking in an interview"></div>
    <div class="video-meta">
      <h3>Martin Helder</h3>
      <em>Enterprise Architect,<br>Betvanta</em>
      <div class="play"><span class="play-icon"><svg width="10" height="12" viewBox="0 0 10 12"><path d="M1 0l9 6-9 6z" fill="#fff"/></svg></span>Play Video</div>
    </div>
  </div>
  <div class="testimonial">
    <blockquote>Tracvenna’s allowed us to work out and rationalize where our bandwidth costs are going…[and] come up with roadmaps in terms of what is going to save us the most money first….</blockquote>
    <cite>Martin Helder, Enterprise Architect, Betvanta</cite>
    <a class="read-more" href="#">Read the case study»</a>
  </div>
</section>

<section class="news-panel left">
  <h3>Video Poscasts</h3>
  <ul class="news-list">
    <li><b>Feb 12:</b><p><span class="src">TechLedger article: ...</span> Big Data Does Not End with Volmaris</p></li>
    <li><b>Feb 6:</b><p><span class="src">Tracvenna 1.3.1 released....</span> Read the release notes.</p></li>
    <li><b>Jan 19:</b><p><span class="src">ComputeDaily article: ....</span> Betvanta Decides Against Volmaris...</p></li>
  </ul>
  <a class="read-more" href="#">Read More»</a>
</section>

<section class="news-panel right">
  <h3>Video Poscasts</h3>
  <ul class="news-list">
    <li><b>24 Apr:</b><p>Monitoring Heap Profiles in Distributed JVM-based Environments</p></li>
    <li><b>01 Feb:</b><p>Log in to Tracvenna using Corvane Directory Services</p></li>
    <li><b>31 Jan:</b><p>Monitoring Disk Performance</p></li>
  </ul>
  <a class="read-more" href="#">Read More»</a>
</section>

<section class="clients" aria-label="Our customers">
  <ul>
    <li>Betvanta</li>
    <li>Quorvix</li>
    <li>Meridian Labs</li>
    <li>Alpenstadt Bank</li>
  </ul>
</section>

<footer class="site-footer">
  <div class="footer-col" style="left:93px">
    <h4>Product</h4>
    <ul><li>Overview</li><li>Root Cause Analysis</li><li>Monitoring and DevOps</li><li>Release Information</li></ul>
  </div>
  <div class="footer-col" style="left:248px">
    <h4>Help</h4>
    <ul><li>Support</li><li>Documentation</li><li>Forum</li><li>Contact Us</li></ul>
  </div>
  <div class="footer-col" style="left:361px">
    <h4>Try and Buy</h4>
    <ul><li>Pricing</li><li>Download</li><li>Buy</li></ul>
  </div>
  <div class="footer-col connect" style="left:495px">
    <h4>Connect Us</h4>
    <ul><li>Pagespace</li><li>Chatterline</li><li>Careernet</li><li>Clipstream</li></ul>
  </div>
  <p class="copyright">Copyright ©2013.Tracvenna.<br>All Right Reserved</p>
</footer>

</body>
</html>
```